New Company Business Card Design

I have a new company logo and I want a new business card design. I dont know if the logo file i attached is in the correct format or quality. We are a New York City Specialty construction Firm specializing in high risk out of the box projects. I want a simple and classy business card that people will his card is as crisp as the work his company does.

Target Market(s)

Clients in the heavy construction industry in New York City

Industry/Entity Type

Construction Company

Contact Information for Business Card

Simple Classy - DIFFERENT

Font styles to use
Other font styles liked:
• Mach the logo font in some way

Colors

Designer to choose colors to be used in the design.

Requirements
Must have
• Uniqueness
Nice to have
• Nothing particular - Just different and classy - Timeless
Should not have
• Goofy Shit or Gimmicky shit

```html
<!DOCTYPE html>
<html lang="en">
<head>
<meta charset="utf-8">
<title>Halvorsen Group – Business Cards</title>
<link href="https://fonts.googleapis.com/css2?family=Arimo:wght@400;700&display=swap" rel="stylesheet">
<style>
  :root {
    --stage: #e4e4e4;
    --blue-light: #0a90cb;
    --blue-mid: #0878bd;
    --blue-deep: #0b5aab;
    --ink: #1c1c1c;
    --bar: #111111;
    --label: #1f5fb4;
    --paper: #ffffff;
    --paper-shade: #ececec;
    --ghost: rgba(0, 0, 0, 0.04);
  }
  * { box-sizing: border-box; margin: 0; padding: 0; }
  html, body { width: 1200px; height: 804px; overflow: hidden; }
  body {
    background: var(--stage);
    font-family: "Arimo", Arial, sans-serif;
    color: var(--ink);
    position: relative;
  }
  .card {
    position: absolute;
    width: 494px;
    height: 282px;
    overflow: hidden;
  }
  .card--front-a { left: 86px; top: 64px; background: linear-gradient(100deg, var(--paper-shade) 0%, var(--paper) 55%, var(--paper-shade) 100%); }
  .card--back-a  { left: 619px; top: 64px; }
  .card--front-b { left: 86px; top: 467px; background: var(--paper); }
  .card--back-b  { left: 619px; top: 467px; }
  .card--back-a, .card--back-b {
    background: linear-gradient(180deg, var(--blue-light) 0%, var(--blue-mid) 60%, var(--blue-deep) 100%);
  }

  /* wordmark */
  .wordmark {
    position: absolute;
    font-weight: 700;
    text-transform: uppercase;
    letter-spacing: 1px;
    white-space: nowrap;
    line-height: 1;
  }
  .wordmark--blue { color: var(--blue-mid); font-size: 20px; }
  .wordmark--white { color: var(--paper); font-size: 24px; left: 0; right: 0; text-align: center; top: 112px; }
  .ghost-mark {
    position: absolute;
    font-weight: 700;
    font-size: 120px;
    line-height: 1;
    white-space: nowrap;
    color: var(--ghost);
  }

  /* front A */
  .header-band {
    position: absolute; left: 0; top: 0; width: 100%; height: 68px;
    background: linear-gradient(180deg, var(--blue-light), var(--blue-deep));
  }
  .accent-bar { position: absolute; background: var(--bar); height: 11px; }
  .card--front-a .accent-bar { left: 276px; right: 0; top: 68px; }
  .card--back-a .accent-bar { left: 139px; width: 217px; bottom: 0; }
  .person { position: absolute; right: 37px; text-align: right; }
  .person__name { font-size: 21px; font-weight: 700; }
  .person__title { font-size: 14px; margin-top: 3px; }
  .card--front-a .person { top: 17px; color: var(--paper); }
  .card--front-b .person { top: 35px; }
  .card--front-b .person__name { color: var(--blue-deep); }
  .card--front-b .person__title { color: var(--ink); }

  .contact { position: absolute; right: 37px; top: 117px; text-align: right; font-size: 15px; line-height: 19px; }
  .contact__group + .contact__group { margin-top: 19px; }
  .contact__label { color: var(--label); }

  /* front B */
  .swoosh { position: absolute; left: 0; top: 0; }
  .contact-strip {
    position: absolute; left: 0; right: 0; top: 216px;
    text-align: center; color: var(--paper); font-size: 14.5px; line-height: 19px;
  }

  /* backs */
  .tagline {
    position: absolute; left: 0; right: 0; top: 221px;
    text-align: center; color: var(--paper); font-size: 15px; line-height: 20px;
    text-transform: uppercase;
  }
</style>
</head>
<body>

  <!-- Option 1: front -->
  <section class="card card--front-a">
    <span class="ghost-mark" style="left:330px; top:150px;" aria-hidden="true">HG</span>
    <div class="header-band"></div>
    <div class="accent-bar"></div>
    <div class="person">
      <p class="person__name">Marcus Ellery</p>
      <p class="person__title">Partner</p>
    </div>
    <span class="wordmark wordmark--blue" style="left:28px; top:157px;">Halvorsen Group</span>
    <div class="contact">
      <div class="contact__group">
        <p>118 Harbor Ave.</p>
        <p>Bayonne, NJ 07002</p>
      </div>
      <div class="contact__group">
        <p><span class="contact__label">Tel:</span> (201) 555-0142</p>
        <p><span class="contact__label">Fax:</span> (201) 555-0143</p>
      </div>
      <div class="contact__group">
        <p><span class="contact__label">Email:</span> ME@hvgroup.com</p>
        <p><span class="contact__label">Web:</span> www.hvgroup.com</p>
      </div>
    </div>
  </section>

  <!-- Option 1: back -->
  <section class="card card--back-a">
    <span class="wordmark wordmark--white">Halvorsen Group</span>
    <p class="tagline">Steady hands for<br>demanding structures</p>
    <div class="accent-bar"></div>
  </section>

  <!-- Option 2: front -->
  <section class="card card--front-b">
    <svg class="swoosh" width="494" height="282" viewBox="0 0 494 282" aria-hidden="true">
      <defs>
        <linearGradient id="swoosh-blue" x1="0" y1="0" x2="0" y2="1">
          <stop offset="0" stop-color="#0a78c2"/>
          <stop offset="1" stop-color="#0b55a8"/>
        </linearGradient>
      </defs>
      <path d="M0,120 Q250,250 494,104 L494,118 Q260,240 0,160 Z" fill="#111"/>
      <path d="M0,164 Q250,240 494,130 L494,282 L0,282 Z" fill="url(#swoosh-blue)"/>
    </svg>
    <span class="wordmark wordmark--blue" style="left:30px; top:66px;">Halvorsen Group</span>
    <div class="person">
      <p class="person__name">Marcus Ellery</p>
      <p class="person__title">Partner</p>
    </div>
    <div class="contact-strip">
      <p>118 Harbor Ave. Bayonne, NJ 07002</p>
      <p>Tel: (201) 555-0142, Fax: (201) 555-0143</p>
      <p>Email: ME@hvgroup.com, Web: www.hvgroup.com</p>
    </div>
  </section>

  <!-- Option 2: back -->
  <section class="card card--back-b">
    <span class="wordmark wordmark--white">Halvorsen Group</span>
    <p class="tagline">Steady hands for<br>demanding structures</p>
  </section>

</body>
</html>
```